Design an Retro Flash Nightgown Groove Party Flyer

Hi everyone, I am looking for a design to a club flyer. Here are the details to be included on the flyer for this event...

Company Name - Velvet Harbor Ent Presents
Event Name - Retro Flash Nightgown Groove Party!! (columbus day weekend)
Event Date - Friday Oct. 5th
Music By - DJ Marble (Playing nothing but the Hottest!! Hip Hop, Groove Wagon, House, Reggea and so much more!!)
Extra Curricular Activities - Best PJ's Wins Cash Grand Prize
Event Details - Doors Open at 9pm, 21+ Event/ Proper ID is a Must, For More Info Call (508)-471-2938
Social Media -FB https://www.facebook.com/VelvetHarborEnt/
INS https://www.instagram.com/velvetharborent/
Venue - THE LANTERN 17 Bramblewick Ln. Nantucket MA 02554

I've attached two images of flyers that some what resemble what I'm looking for, but feel free to get creative and come up with your own design, the best design will win out. Thank you all for your time, and good luck ;)...

```html
<!DOCTYPE html>
<html lang="en">
<head>
<meta charset="utf-8">
<title>Retro Flash Nightgown Groove Party</title>
<link rel="stylesheet" href="https://fonts.googleapis.com/css2?family=Montserrat:wght@500;600;700;800&family=Righteous&display=swap">
<style>
  :root {
    --gold: #ffd21c;
    --gold-deep: #f2a900;
    --white: #ffffff;
    --ink: #0b0b0b;
    --sky-cyan: #7fe3f5;
    --sky-violet: #b98cf0;
    --sky-pink: #f6a9d8;
    --sky-peach: #ffd3a1;
    --night-blue: #1a2a6c;
    --night-deep: #0a1238;
    --flare-red: #e8262b;
    --flare-orange: #ff8a1a;
    --flare-yellow: #ffe23a;
    --leaf: #3aa84a;
    --link-mark: #e6236f;
  }
  * { margin: 0; padding: 0; box-sizing: border-box; }
  html, body { width: 928px; height: 1200px; overflow: hidden; background: var(--ink); }
  .flyer {
    position: relative; width: 928px; height: 1200px; overflow: hidden;
    font-family: 'Montserrat', Arial, sans-serif; text-align: center;
  }
  .sky {
    position: absolute; left: 0; top: 0; width: 928px; height: 540px;
    background:
      radial-gradient(ellipse at 75% 80%, var(--sky-peach) 0%, transparent 55%),
      linear-gradient(100deg, var(--sky-cyan) 0%, var(--sky-violet) 45%, var(--sky-pink) 75%, var(--sky-peach) 100%);
  }
  .city-scene {
    position: absolute; left: 0; top: 530px; width: 928px; height: 670px;
    background:
      radial-gradient(circle at 80% 20%, rgba(120,200,80,.55) 0%, transparent 30%),
      radial-gradient(circle at 15% 25%, rgba(255,170,40,.55) 0%, transparent 30%),
      radial-gradient(ellipse at 50% 60%, rgba(255,120,40,.35) 0%, transparent 55%),
      linear-gradient(180deg, #3b2a5a 0%, var(--night-blue) 55%, var(--night-deep) 100%);
  }
  .shapes { position: absolute; left: 0; top: 0; }
  .models-photo {
    position: absolute; left: 120px; top: 160px; width: 690px; height: 355px;
    border-radius: 40px 40px 10px 10px;
    background: radial-gradient(ellipse at 50% 55%, rgba(255,120,170,.75) 0%, rgba(200,150,230,.5) 45%, transparent 72%);
  }
  .presenter { position: absolute; top: 50px; left: 0; width: 100%; color: var(--gold); font-weight: 700; }
  .presenter .company { font-size: 31px; letter-spacing: 1px; line-height: 1; }
  .presenter .presents { font-size: 19px; letter-spacing: 1px; margin-top: 3px; }
  .title { position: absolute; top: 550px; left: 0; width: 100%; }
  .title-kicker {
    font-family: 'Righteous', 'Montserrat', sans-serif; font-size: 54px; color: var(--gold);
    -webkit-text-stroke: 3px var(--ink); paint-order: stroke fill; line-height: 1;
  }
  .title-main {
    font-weight: 700; font-size: 80px; line-height: 1.08; letter-spacing: 1px;
    background: linear-gradient(180deg, var(--flare-yellow) 20%, var(--gold-deep) 100%);
    -webkit-background-clip: text; background-clip: text; color: transparent;
    filter: drop-shadow(2px 3px 2px rgba(0,0,0,.55));
    margin-top: 6px;
  }
  .date-pill {
    position: absolute; left: 345px; top: 880px; width: 285px; height: 52px;
    background: var(--ink); border-radius: 26px; color: var(--white);
    font-weight: 600; font-size: 28px; line-height: 52px;
  }
  .info { position: absolute; left: 0; width: 100%; font-weight: 600; }
  .lineup { top: 950px; font-size: 23px; color: var(--white); }
  .lineup .hl { color: var(--gold); }
  .prize { top: 990px; font-size: 21px; color: var(--gold); font-weight: 700; }
  .social { top: 1034px; font-size: 13px; color: var(--white); font-weight: 500; line-height: 24px; }
  .social .dot { display: inline-block; width: 8px; height: 8px; margin-right: 8px; background: var(--link-mark); vertical-align: middle; }
  .doors { top: 1093px; font-size: 17px; color: var(--white); font-weight: 500; }
  .call { top: 1122px; font-size: 20px; color: var(--gold); }
  .venue { top: 1158px; font-size: 14px; color: var(--gold); }
</style>
</head>
<body>
<main class="flyer">
  <div class="sky"></div>
  <div class="city-scene" role="img" aria-label="Night city skyline by the water with fireworks and glowing bokeh lights"></div>

  <svg class="shapes" width="928" height="1200" viewBox="0 0 928 1200" aria-hidden="true">
    <defs>
      <linearGradient id="flare" x1="0" y1="0" x2="1" y2="1">
        <stop offset="0" stop-color="#e8262b"/>
        <stop offset=".45" stop-color="#ff8a1a"/>
        <stop offset="1" stop-color="#ffe23a"/>
      </linearGradient>
      <linearGradient id="prism" x1="0" y1="0" x2="1" y2="0">
        <stop offset="0" stop-color="#6b3bd8"/>
        <stop offset=".5" stop-color="#b43ad0"/>
        <stop offset="1" stop-color="#ff6a4a"/>
      </linearGradient>
    </defs>
    <polygon points="0,255 0,520 140,520" fill="#3aa84a" opacity=".85"/>
    <polygon points="928,330 928,520 820,520" fill="#3aa84a" opacity=".85"/>
    <polygon points="464,85 90,515 838,515" fill="none" stroke="url(#prism)" stroke-width="26" stroke-linejoin="round" opacity=".9"/>
    <polygon points="110,535 830,535 575,1000" fill="url(#flare)" opacity=".82"/>
    <rect x="0" y="515" width="928" height="22" fill="#4a7a3a" opacity=".5"/>
  </svg>

  <div class="models-photo" role="img" aria-label="Five women posing in colourful pajamas, one holding a plush teddy bear"></div>

  <header class="presenter">
    <div class="company">VELVET HARBOR ENT</div>
    <div class="presents">PRESENTS</div>
  </header>

  <h1 class="title">
    <div class="title-kicker">RETRO FLASH</div>
    <div class="title-main">NIGHTGOWN<br>GROOVE PARTY</div>
  </h1>

  <div class="date-pill">FRIDAY OCT. 5TH</div>

  <p class="info lineup">DJ MARBLE | <span class="hl">HIP HOP</span> | GROOVE WAGON | <span class="hl">HOUSE</span> | REGGEA</p>
  <p class="info prize">BEST PJ'S WINS CASH GRAND PRIZE</p>
  <p class="info social">
    <span class="dot"></span>https://www.friendwall.net/VelvetHarborEnt/<br>
    <span class="dot"></span>https://www.snapgrid.net/velvetharborent/
  </p>
  <p class="info doors">Doors Open at 9pm, 21+ Event/ Proper ID is a Must, For More Info</p>
  <p class="info call">CALL (508)-471-2938</p>
  <p class="info venue">THE LANTERN 17 Bramblewick Ln. Nantucket MA 02554</p>
</main>
</body>
</html>
```